Logo & Visitenkarte für mobile Fußpflege
Zielgruppe
Meine Firma geht zu den Kunden nach hause und bietet ihnen eine Fusspflege und Massage an in Seewil.
der Titel den ich trage ist Dipl. Fusspflegerin dies aber nur auf der Visitenkarte vermerken. Die Visitenkarte soll auf der Rückseite möglich keit zu haben Termine aufzuschreiben.
Aufgabenstellung
das design soll gut lesbar und unverwechselbar sein, da eher alte Leute eine Fusspflege Buchen soll es schlicht sein. die nummer +41 76 555 18 27

```html
<!DOCTYPE html>
<html lang="de">
<head>
<meta charset="utf-8">
<title>Mobile Fusspflege Lindauer Seewil – Visitenkarte</title>
<link rel="stylesheet" href="https://fonts.googleapis.com/css2?family=Montserrat:wght@700&family=Roboto:wght@400;500&family=Questrial&display=swap">
<style>
  :root {
    --backdrop: #a6b4b9;
    --card-back: #8b5390;
    --card-front: #7a4381;
    --ink: #f1eef2;
    --ink-faint: #a77cab;
    --rule: #d9c8dc;
  }
  * { box-sizing: border-box; margin: 0; padding: 0; }
  html, body { width: 1200px; height: 1200px; overflow: hidden; }
  body {
    background: var(--backdrop);
    font-family: "Roboto", Arial, sans-serif;
    color: var(--ink);
    position: relative;
  }
  .card {
    position: absolute;
    left: 170px;
    width: 860px;
    height: 500px;
    box-shadow: 0 14px 30px rgba(40, 50, 55, 0.25);
  }
  .card--appointment { top: 70px; background: var(--card-back); display: flex; }
  .card--front { top: 630px; background: var(--card-front); }

  /* Appointment side */
  .stub {
    width: 400px;
    height: 100%;
    padding: 50px 0 44px 48px;
    display: flex;
    flex-direction: column;
    justify-content: space-between;
  }
  .brand { display: flex; align-items: flex-start; gap: 14px; }
  .brand__dot {
    width: 14px; height: 14px; border-radius: 50%;
    background: var(--ink); margin-top: 5px; flex: none;
  }
  .brand__name {
    font-family: "Montserrat", Arial, sans-serif;
    font-weight: 700;
    text-transform: uppercase;
    color: var(--ink);
    line-height: 1.15;
  }
  .stub .brand__name { font-size: 17px; letter-spacing: 1px; }
  .brand__phone {
    font-family: "Questrial", Arial, sans-serif;
    letter-spacing: 2px;
    margin-top: 6px;
  }
  .stub .brand__phone { font-size: 14px; }

  .contact { list-style: none; font-size: 15px; }
  .contact li { display: flex; align-items: center; gap: 14px; margin-top: 10px; }
  .contact svg { width: 20px; height: 20px; flex: none; }

  .perforation {
    width: 0;
    height: 100%;
    border-left: 3px dashed var(--ink);
    opacity: 0.9;
  }

  .slip { flex: 1; padding: 56px 56px 44px 44px; display: flex; flex-direction: column; }
  .slip__title {
    font-family: "Questrial", Arial, sans-serif;
    font-size: 46px;
    letter-spacing: 3px;
    font-weight: 400;
  }
  .field { margin-top: 38px; border-bottom: 1.5px solid var(--rule); padding-bottom: 6px; }
  .field__label { font-weight: 500; font-size: 24px; color: var(--ink-faint); }
  .slip__note { margin-top: auto; font-size: 19px; line-height: 1.35; max-width: 300px; }

  /* Front side */
  .card--front { display: flex; align-items: center; justify-content: center; }
  .card--front .brand { gap: 22px; }
  .card--front .brand__dot { width: 28px; height: 28px; margin-top: 8px; }
  .card--front .brand__name { font-size: 40px; letter-spacing: 2px; }
  .card--front .brand__phone { font-size: 32px; margin-top: 12px; }
</style>
</head>
<body>

<section class="card card--appointment" aria-label="Terminkarte">
  <div class="stub">
    <div class="brand">
      <span class="brand__dot"></span>
      <div>
        <p class="brand__name">Mobile Fusspflege<br>Lindauer Seewil</p>
        <p class="brand__phone">+41 76 555 18 27</p>
      </div>
    </div>
    <ul class="contact">
      <li>
        <svg viewBox="0 0 24 24" fill="var(--ink)" aria-hidden="true"><path d="M6.6 10.8a15 15 0 0 0 6.6 6.6l2.2-2.2c.3-.3.7-.4 1-.2 1.1.4 2.3.6 3.6.6.6 0 1 .4 1 1V20c0 .6-.4 1-1 1A17 17 0 0 1 3 4c0-.6.4-1 1-1h3.5c.6 0 1 .4 1 1 0 1.3.2 2.5.6 3.6.1.3 0 .7-.2 1z"/></svg>
        <span>+41 76 555 18 27</span>
      </li>
      <li>
        <svg viewBox="0 0 24 24" fill="none" stroke="var(--ink)" stroke-width="2" aria-hidden="true"><circle cx="12" cy="12" r="9"/><path d="M3 12h18M12 3c3 3 3 15 0 18M12 3c-3 3-3 15 0 18"/></svg>
        <span>sanftschritt.ch</span>
      </li>
      <li>
        <svg viewBox="0 0 24 24" fill="var(--ink)" aria-hidden="true"><path d="M2 5h20v14H2z" fill="none" stroke="var(--ink)" stroke-width="2"/><path d="M2 5l10 8 10-8"/></svg>
        <span>info@sanftschritt.ch</span>
      </li>
    </ul>
  </div>

  <div class="perforation" aria-hidden="true"></div>

  <div class="slip">
    <h2 class="slip__title">APPOINTMENT</h2>
    <div class="field"><span class="field__label">Date</span></div>
    <div class="field"><span class="field__label">Time</span></div>
    <p class="slip__note">If you are unable to keep your appointment, please contact us.</p>
  </div>
</section>

<section class="card card--front" aria-label="Vorderseite">
  <div class="brand">
    <span class="brand__dot"></span>
    <div>
      <p class="brand__name">Mobile Fusspflege<br>Lindauer Seewil</p>
      <p class="brand__phone">+41 76 555 18 27</p>
    </div>
  </div>
</section>

</body>
</html>
```